Crestavo Clear Max information sheet

Looking for a front/back information brochure to be handed out to customers for our water treatment chemical. We have a brochure but would like it updated with a more professional look. We are not locked into the style on the attached and want some fresh ideas. We would like to have the final design in Adobe Illustrator so we can modify it in the future if necessary.
We have an Adobe Stock account so have access to all of those photos/images.

```html
<!DOCTYPE html>
<html lang="en">
<head>
<meta charset="utf-8">
<title>Crestavo Clear Max – Information Sheet</title>
<link rel="stylesheet" href="https://fonts.googleapis.com/css2?family=Saira+Semi+Condensed:wght@500;600;700&display=swap">
<style>
  :root {
    --stage: #dfe9ea;
    --paper: #eef2f6;
    --photo-light: #f3f6f9;
    --photo-mid: #cfdbe6;
    --photo-deep: #b3c6d6;
    --wave-blue: #2a83c6;
    --brand-blue: #1f6fc0;
    --white: #ffffff;
  }
  * { box-sizing: border-box; margin: 0; padding: 0; }
  html, body {
    width: 1200px; height: 908px; overflow: hidden;
    background: var(--stage);
  }
  .canvas {
    position: relative; width: 1200px; height: 908px;
    display: flex; align-items: center; justify-content: center;
  }
  .cover {
    position: relative; width: 666px; height: 862px;
    background: var(--paper); overflow: hidden;
    font-family: "Saira Semi Condensed", sans-serif;
    box-shadow: 0 10px 30px rgba(40, 70, 80, 0.18);
  }
  .cover-photo {
    position: absolute; inset: 0;
    background:
      radial-gradient(ellipse 30% 22% at 56% 42%, rgba(255,255,255,0.75), transparent 70%),
      radial-gradient(ellipse 60% 30% at 50% 62%, var(--photo-deep), transparent 75%),
      linear-gradient(160deg, var(--photo-light) 0%, var(--photo-mid) 55%, var(--photo-light) 100%);
  }
  .brand-block {
    position: absolute; top: 54px; left: 240px; width: 330px;
    text-align: center;
  }
  .brand-tagline {
    font-size: 14px; font-weight: 500; letter-spacing: 0.02em;
    color: var(--brand-blue); text-transform: uppercase;
    white-space: nowrap;
  }
  .brand-name {
    font-size: 32px; font-weight: 700; line-height: 1.1;
    color: var(--brand-blue); text-transform: uppercase;
    white-space: nowrap;
  }
  .maker {
    margin-top: 8px;
    font-size: 14px; font-weight: 500; letter-spacing: 0.02em;
    color: var(--brand-blue); white-space: nowrap;
  }
  .cover-wave {
    position: absolute; left: 0; bottom: 0; width: 666px; height: 360px;
  }
  .cover-title {
    position: absolute; right: 70px; bottom: 104px;
    color: var(--white); font-weight: 600; font-size: 38px; line-height: 1.12;
    text-align: right; white-space: nowrap;
  }
  .cover-title span { display: block; }
</style>
</head>
<body>
<main class="canvas">
  <article class="cover">
    <div class="cover-photo" role="img" aria-label="Photograph of clear water bubbles with molecule structures inside, splashing over a pale blue background"></div>

    <header class="brand-block">
      <p class="brand-tagline">Water Treatment Concentrate</p>
      <h1 class="brand-name">Crestavo Clear Max</h1>
      <p class="maker">Norwell Supply Co.</p>
    </header>

    <svg class="cover-wave" viewBox="0 0 666 360" preserveAspectRatio="none" aria-hidden="true">
      <path fill="var(--wave-blue)" d="M0 210 C 90 130, 170 160, 240 150 C 320 138, 380 205, 470 160 C 560 115, 610 40, 666 20 L 666 360 L 0 360 Z"/>
    </svg>

    <h2 class="cover-title">
      <span>Next Generation</span>
      <span>Oxidation Technology</span>
    </h2>
  </article>
</main>
</body>
</html>
```